4th Generation Family Business Needs a New Card Design!

We are a family owned 4th Generation company. We are based in the Sydney, Australia area and we are desperately in need of a more modern and classy card. We are monumental masons who design, supply & erect lasting memorials throughout cemeteries in Sydney. Our customers are normally in a period of grieving. I have attached logo files that will need to be implemented on the card. Company was established 1935. Australian Owned and Operated. Card needs to be designed to PRINTLY.com specification.

Target Market(s)

Our target market is based upon people that a grieving for family members that have passed away. We also deal with alot of companies that own and operate cemeteries.

Industry/Entity Type

Business

Contact Information for Business Card

Gavin Pelham, Operations Manager, 0491726053, gavin@pelhamstoneworks.com.au
Brian Pelham, Director, 0417639285, brian@pelhamstoneworks.com.au
Phone # 02 9563 4820
Website: www.pelhamstoneworks.com.au
Address: Suite 17, 9 Lambert Lane, Kellyville, Sydney NSW 2155

Font styles to use
Serif
Decorative
Script

Requirements
Must have
• Would like to see the logo nicely implemented with a modern design. Embossed lettering would be a nice additive.

```html
<!DOCTYPE html>
<html lang="en">
<head>
<meta charset="utf-8">
<title>Pelham Stoneworks — Business Card</title>
<link rel="stylesheet" href="https://fonts.googleapis.com/css2?family=Cinzel:wght@400;600&family=Tinos&display=swap">
<style>
  :root {
    --backdrop: #e3e3e3;
    --card-black: #0b0c0e;
    --card-sheen: #2a2b2e;
    --paper: #f6f6f4;
    --gold: #e8b70f;
    --gold-deep: #c99a0a;
    --ink-light: #f2f2f2;
    --ink-dark: #141414;
  }
  * { margin: 0; padding: 0; box-sizing: border-box; }
  html, body { width: 1200px; height: 576px; overflow: hidden; }
  body { background: var(--backdrop); position: relative; font-family: "Tinos", "Times New Roman", serif; }

  .card {
    position: absolute;
    top: 138px;
    width: 484px;
    height: 294px;
    overflow: hidden;
    box-shadow: 0 2px 5px rgba(0,0,0,0.35);
  }

  /* Front */
  .card--front {
    left: 81px;
    background:
      linear-gradient(90deg, transparent 22%, rgba(70,72,76,0.35) 30%, transparent 40%, transparent 60%, rgba(60,62,66,0.3) 66%, transparent 74%),
      var(--card-black);
  }
  .front-band {
    position: absolute; left: 0; right: 0; bottom: 0; height: 10px;
    background: linear-gradient(90deg, var(--gold-deep), var(--gold), var(--gold-deep));
  }
  .wordmark {
    position: absolute;
    font-family: "Cinzel", serif;
    font-weight: 400;
    text-align: center;
    line-height: 1.05;
    letter-spacing: 1px;
  }
  .card--front .wordmark {
    left: 0; right: 0; top: 108px;
    color: var(--ink-light);
    font-size: 34px;
  }
  .wordmark span { display: block; font-size: 0.62em; letter-spacing: 3px; margin-top: 4px; }

  /* Back */
  .card--back {
    left: 602px;
    background:
      linear-gradient(90deg, transparent 35%, rgba(70,72,76,0.3) 45%, transparent 55%),
      var(--card-black);
  }
  .back-shapes { position: absolute; inset: 0; }
  .card--back .wordmark {
    left: 252px; width: 232px; top: 110px;
    color: var(--ink-dark);
    font-size: 29px;
  }
  .holder-name {
    position: absolute; left: 22px; top: 20px;
    font-family: "Cinzel", serif; font-weight: 600;
    font-size: 19px; letter-spacing: 0.5px;
    color: var(--gold);
  }
  .holder-role {
    position: absolute; left: 22px; top: 44px;
    font-size: 11.5px; color: var(--ink-light);
  }
  .address {
    position: absolute; left: 22px; top: 162px;
    font-size: 12px; line-height: 17px; color: var(--ink-light);
  }
  .contacts {
    position: absolute; left: 22px; top: 206px;
    list-style: none;
    font-size: 12px; line-height: 17px; color: var(--ink-light);
  }
  .contacts li { display: flex; align-items: center; gap: 8px; }
  .contacts svg { width: 9px; height: 9px; fill: var(--gold); flex: none; }
</style>
</head>
<body>

<section class="card card--front" aria-label="Card front">
  <div class="wordmark">Pelham<span>Stoneworks</span></div>
  <div class="front-band"></div>
</section>

<section class="card card--back" aria-label="Card back">
  <svg class="back-shapes" viewBox="0 0 484 294" preserveAspectRatio="none" aria-hidden="true">
    <path d="M322 0 Q232 120 294 294 L300 294 Q248 130 336 0 Z" fill="var(--gold)"/>
    <path d="M336 0 Q248 130 300 294 L484 294 L484 0 Z" fill="var(--paper)"/>
  </svg>

  <h1 class="holder-name">Gavin Pelham</h1>
  <p class="holder-role">Operations Manager</p>

  <p class="address">Suite 17, 9 Lambert Lane,<br>Kellyville, Sydney NSW 2155</p>

  <ul class="contacts">
    <li><svg viewBox="0 0 10 10"><path d="M2 0.5 L4 2.5 L3 4 Q4.5 6 6 7 L7.5 6 L9.5 8 L8 9.5 Q3 9 0.5 2 Z"/></svg>0417639285</li>
    <li><svg viewBox="0 0 10 10"><path d="M0 3 Q5 0 10 3 L10 4.5 L7.5 4.5 L7 3.5 L3 3.5 L2.5 4.5 L0 4.5 Z M2 5.5 L8 5.5 L9 9.5 L1 9.5 Z"/></svg>02 9563 4820</li>
    <li><svg viewBox="0 0 10 10"><path d="M0 2 L10 2 L5 6 Z M0 3 L5 7 L10 3 L10 8.5 L0 8.5 Z"/></svg>brian@pelhamstoneworks.com.au</li>
    <li><svg viewBox="0 0 10 10"><circle cx="5" cy="5" r="4.5"/></svg>www.pelhamstoneworks.com.au</li>
  </ul>

  <div class="wordmark">Pelham<span>Stoneworks</span></div>
</section>

</body>
</html>
```